디자인 카테고리
라벨(파우치) (일반/기타 업종)
브랜드 소개
가람식품은 15년 역사를 가진 건강식품 회사입니다.
사람과 자연을 생각하는 정직하고 행복한 회사이며, 정직한 원료로 정직하게 생산하고 정직하게 판매하는 업체로써, 이번에 [그린커피빈가루/환]신제품 출시예정으로 이 제품의 패키지 스티커 디자인 공모를 개최하게 되었습니다.

```html
<!DOCTYPE html>
<html lang="ko">
<head>
<meta charset="utf-8">
<title>그린커피빈 환 라벨</title>
<link href="https://fonts.googleapis.com/css2?family=Oswald:wght@500;700&family=Noto+Sans+KR:wght@400;500;700&display=swap" rel="stylesheet">
<style>
  :root {
    --bg: #e9eaea;
    --label: #ffffff;
    --lime: #9cb71c;
    --lime-dark: #6f8a0e;
    --lime-soft: #e4ecc2;
    --ink: #3a3a3a;
    --stripe: #eef2e2;
  }
  * { margin: 0; padding: 0; box-sizing: border-box; }
  html, body { width: 1200px; height: 1200px; overflow: hidden; background: var(--bg); }
  .canvas { position: relative; width: 1200px; height: 1200px; }
  .label {
    position: absolute; left: 150px; top: 220px; width: 900px; height: 760px;
    background: var(--label); box-shadow: 0 10px 30px rgba(0,0,0,.08);
  }
  .label-art { position: absolute; inset: 0; }
  .leaf-mark {
    position: absolute; left: 412px; top: 85px; width: 76px; height: 52px;
    background: var(--lime); border-radius: 50% 50% 40% 40%;
  }
  .product-title {
    position: absolute; left: 0; right: 0; top: 160px; text-align: center;
    font-family: "Oswald", sans-serif; font-weight: 700; font-size: 118px;
    line-height: 1.02; color: var(--lime); letter-spacing: 2px;
  }
  .product-name {
    position: absolute; left: 0; right: 0; top: 568px; text-align: center;
    font-family: "Noto Sans KR", sans-serif; font-weight: 400; font-size: 54px;
    line-height: 1.2; color: var(--ink); letter-spacing: -1px;
  }
  .product-name .form { color: var(--lime); font-weight: 500; }
  .net-weight {
    position: absolute; left: 40px; top: 672px;
    font-family: "Noto Sans KR", sans-serif; font-size: 42px; line-height: 1.2; color: var(--ink);
  }
  .origin-stamp {
    position: absolute; left: 650px; top: 70px; width: 180px; height: 180px;
    border: 4px solid var(--lime-dark); border-radius: 50%;
    transform: rotate(-14deg); background: rgba(255,255,255,.9);
    display: flex; flex-direction: column; align-items: center; justify-content: center;
    font-family: "Noto Sans KR", sans-serif; color: var(--lime-dark);
  }
  .origin-stamp::before {
    content: ""; position: absolute; inset: 8px; border: 2px solid var(--lime-dark); border-radius: 50%;
  }
  .origin-stamp .stamp-top { font-size: 20px; font-weight: 500; }
  .origin-stamp .stamp-value { font-family: "Oswald", sans-serif; font-size: 54px; font-weight: 700; line-height: 1; }
  .origin-stamp .stamp-bottom { font-size: 20px; font-weight: 500; }
</style>
</head>
<body>
<main class="canvas">
  <section class="label">
    <svg class="label-art" width="900" height="760" viewBox="0 0 900 760">
      <rect class="stripe-field" x="0" y="0" width="900" height="760" fill="var(--stripe)" role="img" aria-label="연한 세로 줄무늬 배경"/>
      <polygon class="hex-frame" points="450,30 830,180 830,590 450,745 70,590 70,180"
               fill="#ffffff" stroke="var(--lime)" stroke-width="16" stroke-linejoin="miter"/>
      <polygon class="hex-inner" points="450,52 810,194 810,576 450,722 90,576 90,194"
               fill="none" stroke="var(--lime-soft)" stroke-width="4"/>
    </svg>
    <div class="leaf-mark" role="img" aria-label="잎사귀 아이콘"></div>
    <h1 class="product-title">GREEN<br>COFFEE<br>BEAN</h1>
    <p class="product-name">그린커피빈 <span class="form">환</span></p>
    <p class="net-weight">150g</p>
    <div class="origin-stamp">
      <span class="stamp-top">그린커피빈</span>
      <span class="stamp-value">100%</span>
      <span class="stamp-bottom">(인도산)</span>
    </div>
  </section>
</main>
</body>
</html>
```